Collectibles expert needs a new business card design.

My current business card makes me look to high end. It may even make me look arrogant or too stuffy. I do work with high end clients and their items but most of my business is with average people with average items. My business name is Walter Brumby's Old Mill Digging Co. The idea was that I mine the streets helping people discover the treasures buried in their homes. That could be art, jewelry, coins, etc. The name and an older logo I used does not make immediate sense to most people. I tried to go with just my picture and name and that is the current card I am changing. I help people who need to downsize. Whether they are getting rid of one item, a collection or a house full of items I help them discover what they have, what it is worth and what are the best ways we can get the most for them. This may be a combination of estate sale (which I dont do) auction or sell directly to a dealer or collector. Usually it is a combination of these. My main goal is to help make sure they dont accidently sell a Vandermeer painting in a garage sale. I am uploading a copy of my old card and the old logo I used to use but the winning card design will need to be much different than these. You can learn a little more about me at www.walterkbrumby.example, www.oldmilldigng.example and www.facebook.com/omdco. I hope someone can look at what I do and come up with a very unique design that will be equally effective if my client is high income or if my client is low to mid income. I do not care if it is a one or two sided card as long as it conveys my contact information and a good representation of what I do.

Target Market(s)

People who are getting rid of items. These can be elderly couples or individuals that are moving to an active living community and will have less space so they need to sell items. This can also include the children of elder parents that dont want their stuff and want to find solutions to help them get rid of their items.

Contact Information for Business Card

The card should have my business name Walter Brumby's Old Mill Digging Co., phone number 555-312-70981, email walter@oldmilldigging.example and website www.oldmilldigging.example. Would also like to include Buyer, Broker, Consultant and Appraiser. We can put Walter K. Brumby, ISA on the opposite side of the company name since it includes my name as well.

Font styles to use
Sans Serif

Colors

Designer to choose colors to be used in the design.

Requirements
Must have
• My project must have a professional look. It must not alienate low income clients and should still be appealing to high value clients.

```html
<!DOCTYPE html>
<html lang="en">
<head>
<meta charset="utf-8">
<title>Walter Brumby's Old Mill Digging Co. — Business Card</title>
<link rel="stylesheet" href="https://fonts.googleapis.com/css2?family=Lato:ital,wght@0,400;0,700;1,400&display=swap">
<style>
  :root {
    --page-bg: #e9e6e3;
    --ink: #3a1812;
    --ink-soft: #4a2a22;
    --card-light: #ffffff;
    --card-shade: #dcdcdc;
    --copper: #b8744a;
    --copper-deep: #94593a;
    --art-blue: #6f97c2;
    --art-red: #6e1e18;
  }
  * { box-sizing: border-box; margin: 0; padding: 0; }
  html, body { width: 1200px; height: 900px; overflow: hidden; }
  body {
    background: var(--page-bg);
    font-family: "Lato", sans-serif;
    display: flex;
    align-items: center;
    justify-content: center;
    gap: 40px;
  }
  .card {
    width: 560px;
    height: 320px;
    border-radius: 18px;
    position: relative;
    overflow: hidden;
    box-shadow: 0 10px 28px rgba(0,0,0,0.18);
  }
  .card--front {
    background: linear-gradient(150deg, var(--card-shade) 0%, var(--card-light) 45%, var(--card-light) 100%);
  }
  .card--back {
    background: linear-gradient(135deg, var(--copper) 0%, var(--copper-deep) 100%);
  }
  .contact-block {
    position: absolute;
    left: 40px;
    top: 38px;
    width: 305px;
    color: var(--ink);
  }
  .business-name {
    font-weight: 700;
    font-size: 20px;
    line-height: 25px;
    letter-spacing: 1.2px;
    text-transform: uppercase;
  }
  .business-name__line { display: block; white-space: nowrap; }
  .owner-roles {
    font-size: 14px;
    color: var(--ink-soft);
    margin-top: 5px;
    white-space: nowrap;
  }
  .divider {
    width: 22px;
    height: 2px;
    background: var(--ink);
    margin: 13px 0;
  }
  .contact-list { list-style: none; }
  .contact-item {
    display: flex;
    align-items: center;
    gap: 9px;
    font-size: 14px;
    line-height: 22px;
    color: var(--ink-soft);
    white-space: nowrap;
  }
  .contact-icon { width: 11px; height: 11px; flex: none; }
  .miner-art {
    position: absolute;
    right: 28px;
    bottom: 18px;
    width: 165px;
    height: 190px;
    border-radius: 8px;
    background: linear-gradient(160deg, var(--art-blue) 0%, var(--art-blue) 40%, var(--art-red) 60%, var(--art-red) 100%);
    opacity: 0.9;
  }
  .card--back .miner-art {
    right: auto;
    left: 197px;
    bottom: 65px;
  }
</style>
</head>
<body>
  <section class="card card--front">
    <div class="contact-block">
      <h1 class="business-name">
        <span class="business-name__line">Walter Brumby's</span>
        <span class="business-name__line">Old Mill Digging Co.</span>
      </h1>
      <p class="owner-roles">Buyer, Broker, Consultant, Appraiser</p>
      <div class="divider"></div>
      <ul class="contact-list">
        <li class="contact-item">
          <svg class="contact-icon" viewBox="0 0 12 12"><path d="M2.5 1 L4.5 1 L5 3.5 L3.8 4.5 Q4.8 6.8 7.3 8.2 L8.4 7 L11 7.5 L11 9.5 Q10.5 11 9 11 Q2 10 1 3 Q1 1.5 2.5 1 Z" fill="var(--ink)"/></svg>
          555-312-70981,
        </li>
        <li class="contact-item">
          <svg class="contact-icon" viewBox="0 0 12 12"><rect x="1" y="2.5" width="10" height="7" fill="none" stroke="var(--ink)" stroke-width="1.2"/><path d="M1 2.5 L6 6.5 L11 2.5" fill="none" stroke="var(--ink)" stroke-width="1.2"/></svg>
          walter@oldmilldigging.example
        </li>
        <li class="contact-item">
          <svg class="contact-icon" viewBox="0 0 12 12"><circle cx="6" cy="6" r="5" fill="var(--ink)"/><path d="M1 6 H11 M6 1 Q3 6 6 11 M6 1 Q9 6 6 11" fill="none" stroke="#fff" stroke-width="0.7"/></svg>
          www.oldmilldigging.example
        </li>
      </ul>
    </div>
    <div class="miner-art" role="img" aria-label="Painted illustration of a woman miner with a pickaxe seated on an ore cart full of gold"></div>
  </section>

  <section class="card card--back">
    <div class="miner-art" role="img" aria-label="Painted illustration of a woman miner with a pickaxe seated on an ore cart full of gold"></div>
  </section>
</body>
</html>
```